Sales sheet for printing and embroidery apparel items - Cedar Hollow Prints

I would like a one page flyer or sales sheet that I would use as a template to send different images of apparel we produce. I have attached examples of layouts I like.
- Ideally, it would have space for 3-5 items.
- I would like it one page only - not a folding flyer.
- Our companies name is Cedar Hollow Prints.
- This will be used for many different products and markets so I don't need wording/copy. You can use wording from the 7z2 or K81 flyer.

Colors
0054AA
0677BA
7BADD7
CADEEF
E8F1F8
00AB8E
00BBA5
67D7C9
C6EFE9
E9F9F6
FFC000
F8CF3A
FAE287
FDF2CF
FEFAEE

Requirements
Must have
• Places for between 3 and 5 images of apparel (t-shirts, hats etc)

```html
<!DOCTYPE html>
<html lang="en">
<head>
<meta charset="utf-8">
<title>Cedar Hollow Prints – Sales Sheet</title>
<link href="https://fonts.googleapis.com/css2?family=Oswald:wght@600;700&family=Poppins:wght@500;600&display=swap" rel="stylesheet">
<style>
:root{
  --navy:#00365C;
  --coral:#EF5F5F;
  --coral-deep:#E5694A;
  --orange:#E8663E;
  --blush:#FDE8E2;
  --blush-deep:#FAD6CC;
  --white:#FFFFFF;
  --stage:#B8B8B8;
  --ink:#111111;
  --badge:#D9DDE3;
}
*{margin:0;padding:0;box-sizing:border-box}
html,body{width:861px;height:1200px;overflow:hidden;background:var(--stage)}
body{position:relative;font-family:"Poppins",sans-serif}
.flyer{position:absolute;left:122px;top:137px;width:617px;height:926px;background:var(--white);overflow:hidden}
.backdrop{position:absolute;left:0;top:0;width:617px;height:926px}
.display{font-family:"Oswald",sans-serif;font-weight:700;line-height:1;white-space:nowrap}
.cond{display:inline-block}

.headline-line{position:absolute;left:26px;font-size:51px;transform-origin:left top}
.headline-line.one{top:23px;color:var(--white);transform:scaleX(.76)}
.headline-line.two{top:68px;color:var(--coral);transform:scaleX(.84)}

.brand{position:absolute;left:500px;top:16px;width:110px;text-align:center}
.brand-mark{width:68px;height:58px;background:var(--coral);margin:0 auto 6px}
.brand-name{color:var(--navy);font-weight:600;font-size:13px;line-height:1.1}

.features{position:absolute;left:0;top:133px;width:617px}
.feature{position:absolute;width:160px;text-align:center;transform:translateX(-50%)}
.feature svg{display:block;margin:0 auto;width:62px;height:58px}
.feature h3{font-family:"Oswald",sans-serif;font-weight:600;color:var(--coral);font-size:22px;margin-top:6px;line-height:1;white-space:nowrap}
.feature h3 .cond{transform:scaleX(.78)}
.feature p{color:var(--white);font-size:12px;line-height:14px;margin-top:6px;font-weight:500;white-space:nowrap}

.offer-title{position:absolute;left:0;width:617px;top:309px;text-align:center;color:var(--white);font-size:49px;text-shadow:1px 2px 2px rgba(0,0,0,.35)}
.offer-title .cond{transform:scaleX(.88)}
.offer-list{position:absolute;list-style:none;color:var(--white);font-weight:600;font-size:17.5px;line-height:1;white-space:nowrap}
.offer-list li{display:flex;align-items:center;height:27px}
.offer-list .tick{width:16px;height:16px;margin-right:12px;flex:none}
.offer-left{left:29px;top:373px}
.offer-right{left:198px;top:373px}

.section-title{position:absolute;left:0;width:617px;text-align:center;color:var(--navy)}
.section-title span.accent{color:var(--orange)}
.products-title{top:517px;font-size:35px}
.products-title .cond{transform:scaleX(.855)}
.products{position:absolute;left:26px;top:568px;display:flex;gap:6px}
.product-slot{width:108px;height:97px;background:var(--white);border:1px solid var(--navy)}
.order-title{top:683px;font-size:34.5px}
.order-title .cond{transform:scaleX(.8)}

.step{position:absolute;top:730px}
.step-icon{position:absolute;top:2px;left:0;width:48px;height:48px;border-radius:50%;border:1px solid var(--coral);display:flex;align-items:center;justify-content:center}
.step-icon div{width:42px;height:42px;border-radius:50%;background:var(--navy);display:flex;align-items:center;justify-content:center}
.step-text{position:absolute;top:0}
.step h4{font-size:13px;font-weight:600;color:var(--ink);line-height:1;white-space:nowrap}
.step p{font-size:9px;font-weight:500;color:var(--ink);line-height:10.7px;margin-top:4px;white-space:nowrap}

.footer{position:absolute;left:0;top:822px;width:617px;height:104px;background:var(--navy)}
.footer-cta{position:absolute;left:21px;top:9px;color:var(--coral);font-size:28px;font-weight:600;transform:scaleX(.82);transform-origin:left top}
.contact{position:absolute;left:24px;display:flex;align-items:center;color:var(--white);line-height:1;white-space:nowrap}
.contact.phone{top:41px;font-family:"Oswald",sans-serif;font-weight:600;font-size:26px}
.contact.email{top:70px;font-weight:500;font-size:16px}
.contact svg{margin-right:9px;flex:none}
.social{position:absolute;top:10px;right:21px;display:flex;gap:4px}
.social span{width:21px;height:21px;border-radius:50%;background:var(--coral-deep)}
.badges{position:absolute;left:277px;top:39px;width:319px;height:48px;background:var(--white);border-radius:10px;display:flex;align-items:center;justify-content:space-around;padding:0 14px}
.badge{background:var(--badge)}
.badge.round{width:28px;height:28px;border-radius:50%}
.badge.wide{width:60px;height:22px;border-radius:2px}
.badge.mid{width:40px;height:20px;border-radius:10px}
</style>
</head>
<body>
<main class="flyer">
  <svg class="backdrop" viewBox="0 0 617 926" aria-hidden="true">
    <defs>
      <linearGradient id="coralFade" x1="0" y1="0" x2="0" y2="1">
        <stop offset="0" stop-color="#EF5F5F"/>
        <stop offset="1" stop-color="#E5694A"/>
      </linearGradient>
    </defs>
    <path fill="var(--blush)" d="M0 380 L150 270 H470 L617 380 V520 Q560 580 617 660 V822 H0 V660 Q57 580 0 520 Z"/>
    <circle cx="309" cy="760" r="95" fill="var(--blush-deep)" opacity=".6"/>
    <path fill="var(--navy)" d="M0 0 H617 V281 L429 332 L309 300 L191 332 L0 281 Z"/>
    <path fill="var(--white)" d="M463 0 H617 V138 C585 146 545 132 485 106 Q463 96 463 72 Z"/>
    <path fill="url(#coralFade)" d="M4 375
      L100 306 Q128 286 156 306 L191 332
      L280 274 Q309 255 338 274 L429 332
      L464 306 Q492 286 520 306 L613 375
      Q624 389 613 403 L520 474 Q492 496 464 474 L418 442
      L338 494 Q309 512 280 494 L200 442
      L156 474 Q128 496 100 474 L4 403
      Q-7 389 4 375 Z"/>
  </svg>

  <h1>
    <span class="headline-line one display">ORDER SHIRTS FOR YOUR</span>
    <span class="headline-line two display">ALL OF YOUR RETREATS</span>
  </h1>

  <div class="brand">
    <div class="brand-mark"></div>
    <div class="brand-name">Cedar Hollow Prints</div>
  </div>

  <section class="features">
    <div class="feature" style="left:86px">
      <svg viewBox="0 0 62 58" fill="none" stroke="#fff" stroke-width="1.4" stroke-linejoin="round">
        <path d="M12 30 L30 12 L50 22 L50 38 L32 54 L12 44 Z"/>
        <path d="M12 34 L32 46 L50 30 M12 38 L32 50 L50 34 M12 42 L32 54"/>
        <path d="M24 18 Q30 24 38 18"/>
      </svg>
      <h3><span class="cond">LOW MINIMUMS</span></h3>
      <p>Order as few as 24<br>pieces to get started.</p>
    </div>
    <div class="feature" style="left:233px">
      <svg viewBox="0 0 62 58" fill="none" stroke="#fff" stroke-width="1.4" stroke-linejoin="round">
        <path d="M6 4 L14 6 L30 50"/>
        <circle cx="32" cy="53" r="3"/>
        <path d="M35 50 L60 42"/>
        <rect x="24" y="10" width="16" height="14" transform="rotate(-18 32 17)"/>
        <rect x="30" y="26" width="20" height="16" transform="rotate(-18 40 34)"/>
        <path d="M2 30 H14 M4 36 H16 M2 42 H18"/>
      </svg>
      <h3><span class="cond">FAST TURNAROUND</span></h3>
      <p>2-week standard<br>delivery.</p>
    </div>
    <div class="feature" style="left:374px">
      <svg viewBox="0 0 62 58" fill="none" stroke="#fff" stroke-width="1.4">
        <circle cx="31" cy="12" r="6"/>
        <circle cx="17" cy="16" r="5"/>
        <circle cx="45" cy="16" r="5"/>
        <path d="M22 52 V30 Q22 22 31 22 Q40 22 40 30 V52 M27 52 V38 M35 52 V38"/>
        <path d="M10 46 V30 Q10 24 17 24 M52 46 V30 Q52 24 45 24"/>
      </svg>
      <h3><span class="cond">REAL PEOPLE</span></h3>
      <p>Work with our team<br>of experts and artists.</p>
    </div>
    <div class="feature" style="left:529px">
      <svg viewBox="0 0 62 58" fill="none" stroke="#fff" stroke-width="1.4" stroke-linejoin="round">
        <path d="M31 4 L46 10 V24 Q46 36 31 42 Q16 36 16 24 V10 Z"/>
        <circle cx="31" cy="22" r="8"/>
        <path d="M27 22 L30 25 L35 19"/>
        <path d="M4 42 Q14 38 22 44 H34 Q38 46 34 48 H22 M34 48 L50 44 Q56 44 58 48"/>
        <path d="M8 12 L12 14 M4 22 H10 M54 12 L50 14 M58 22 H52"/>
      </svg>
      <h3><span class="cond">GUARANTEED</span></h3>
      <p>We promise accurate,<br>quality work.</p>
    </div>
  </section>

  <h2 class="offer-title display"><span class="cond">We Offer</span></h2>
  <ul class="offer-list offer-left">
    <li><svg class="tick" viewBox="0 0 17 17"><circle cx="8.5" cy="8.5" r="8.5" fill="var(--navy)"/><path d="M5 8.8 L7.5 11.2 L12 6" stroke="#fff" stroke-width="1.6" fill="none"/></svg>Art Design</li>
    <li><svg class="tick" viewBox="0 0 17 17"><circle cx="8.5" cy="8.5" r="8.5" fill="var(--navy)"/><path d="M5 8.8 L7.5 11.2 L12 6" stroke="#fff" stroke-width="1.6" fill="none"/></svg>Free Shipping</li>
  </ul>
  <ul class="offer-list offer-right">
    <li><svg class="tick" viewBox="0 0 17 17"><circle cx="8.5" cy="8.5" r="8.5" fill="var(--navy)"/><path d="M5 8.8 L7.5 11.2 L12 6" stroke="#fff" stroke-width="1.6" fill="none"/></svg>We Pay ALL Royalties to the Movement</li>
    <li><svg class="tick" viewBox="0 0 17 17"><circle cx="8.5" cy="8.5" r="8.5" fill="var(--navy)"/><path d="M5 8.8 L7.5 11.2 L12 6" stroke="#fff" stroke-width="1.6" fill="none"/></svg>Many Options of Shirt Styles and Colors</li>
  </ul>

  <h2 class="section-title products-title display"><span class="cond">OUR <span class="accent">PRODUCTS</span></span></h2>
  <div class="products">
    <div class="product-slot"></div>
    <div class="product-slot"></div>
    <div class="product-slot"></div>
    <div class="product-slot"></div>
    <div class="product-slot"></div>
  </div>

  <h2 class="section-title order-title display"><span class="cond">HOW TO <span class="accent">START AN ORDER</span></span></h2>

  <div class="step" style="left:15px">
    <div class="step-icon"><div>
      <svg width="22" height="22" viewBox="0 0 22 22" fill="none" stroke="var(--coral)" stroke-width="1.5"><circle cx="13" cy="9" r="6"/><path d="M8.5 13.5 L3 19"/></svg>
    </div></div>
    <div class="step-text" style="left:58px">
      <h4>1. CHOOSE YOUR RIDE</h4>
      <p>Send us a picture, or let us<br>know the make and model<br>of the vehicle you would like<br>featured on your apparel.</p>
    </div>
  </div>

  <div class="step" style="left:217px">
    <div class="step-icon"><div>
      <svg width="22" height="22" viewBox="0 0 22 22" fill="none" stroke="var(--coral)" stroke-width="1.5" stroke-linejoin="round"><path d="M7 3 L2 6 L4 10 L6 9 V19 H16 V9 L18 10 L20 6 L15 3 Q11 7 7 3 Z"/></svg>
    </div></div>
    <div class="step-text" style="left:58px">
      <h4>2. PICK YOUR GEAR</h4>
      <p>We will help you choose<br>your t-shirts, sweatshirts<br>or other apparel items<br>and determine sizes and<br>quantities.</p>
    </div>
  </div>

  <div class="step" style="left:409px">
    <div class="step-icon"><div>
      <svg width="22" height="22" viewBox="0 0 22 22" fill="none" stroke="var(--coral)" stroke-width="1.5" stroke-linecap="round"><path d="M4 18 L18 4 M4 4 L18 18"/></svg>
    </div></div>
    <div class="step-text" style="left:58px">
      <h4>3. WE CUSTOMIZE</h4>
      <p>We make the magic happen<br>and our team of expert artists<br>will design your shirts and get<br>a proof out to you. Upon order<br>approval your order will go<br>into production.</p>
    </div>
  </div>

  <footer class="footer">
    <p class="footer-cta display">We’d love to work with you!</p>
    <p class="contact phone">
      <svg width="17" height="17" viewBox="0 0 17 17"><path fill="var(--coral)" d="M4 1 L7 4 L5.5 6.5 Q7 9.5 10.5 11.5 L13 10 L16 13 L13.5 16 Q7 15 3 10 Q0.5 6 1 3.5 Z"/></svg>
      555-014-2730
    </p>
    <p class="contact email">
      <svg width="15" height="11" viewBox="0 0 15 11"><rect width="15" height="11" fill="var(--coral)"/><path d="M0 0 L7.5 6 L15 0" stroke="var(--navy)" stroke-width="1" fill="none"/></svg>
      sales@chptees.com
    </p>
    <div class="social" aria-label="Social media links"><span></span><span></span><span></span></div>
    <div class="badges" aria-label="Certifications">
      <span class="badge round"></span>
      <span class="badge round"></span>
      <span class="badge wide"></span>
      <span class="badge mid"></span>
      <span class="badge mid"></span>
      <span class="badge mid"></span>
    </div>
  </footer>
</main>
</body>
</html>
```